Marwick Ostrand Law website for a law firm

modern clean website for a small boutique law firm. Based in Sacramento, CA and the Bay Area. Practice areas of Family Law, Civil litigation, and Criminal Defense. We already have a logo design as well as attorney pictures to include on page.
Would like images of California included on site.
Would like site to go with Logo that is already designed...blue/grey/white colors.

Industry/Entity Type

Law Firm

Number of Pages Required

5+ page

Requirements
Must have
• I already have several pages of content drafted. Just need the pages with images to input content. Must be clean and modern feel. Want it to reflect California and small boutique feel that is provided personalized legal attention.
• Must have a page where I can blog or post articles on.

```html
<!DOCTYPE html>
<html lang="en">
<head>
<meta charset="utf-8">
<title>Contact Us | Marwick Ostrand Law</title>
<link rel="stylesheet" href="https://fonts.googleapis.com/css2?family=Open+Sans:wght@400;600;700&family=Raleway:wght@400;500;600&display=swap">
<style>
:root{
  --sky:#4fa2f7;
  --blue:#0a7cf0;
  --title-blue:#1a7ff0;
  --grey:#6f6f70;
  --band-grey:#7b7a7c;
  --logo-grey:#6a6a6c;
  --ink:#1b1b1b;
  --text:#333;
  --form-bg:#f0f0f0;
  --field-border:#9a9a9a;
  --white:#fff;
}
*{box-sizing:border-box;margin:0;padding:0}
html,body{width:708px;height:1200px;overflow:hidden}
body{position:relative;background:var(--white);font-family:"Open Sans",Arial,sans-serif;color:var(--text)}
.abs{position:absolute}
/* top bar */
.top-bar{left:0;top:0;width:708px;height:24px;background:var(--sky)}
.consult-btn{left:457px;top:0;width:200px;height:24px;background:var(--grey);color:var(--white);font-size:10.5px;font-weight:600;display:flex;align-items:center;justify-content:center;gap:6px}
/* header */
.site-header{left:0;top:24px;width:708px;height:58px;background:var(--white)}
.brand{left:49px;top:12px;font-family:"Raleway",sans-serif;font-weight:500;font-size:30px;letter-spacing:1px;color:var(--sky);display:flex;align-items:center;gap:6px}
.brand-mark{width:10px;height:10px;background:var(--sky);border-radius:50%}
.main-nav{left:320px;top:24px;height:33px;display:flex;align-items:center;font-size:10.5px;color:var(--ink)}
.nav-item{display:flex;align-items:center;gap:5px;margin-right:26px}
.nav-item svg{fill:var(--blue)}
.nav-item.active{background:var(--blue);color:var(--white);height:33px;padding:0 9px;margin-right:0}
.nav-item.active svg{fill:var(--white)}
/* hero */
.page-hero{left:0;top:82px;width:708px;height:168px;background:linear-gradient(180deg,#2c3328 0%,#3a4233 45%,#22281f 100%)}
.hero-title{left:49px;top:58px;color:var(--white);font-family:"Raleway",sans-serif;font-size:18.5px}
.hero-rule{left:49px;top:85px;width:100px;height:1.5px;background:var(--white)}
.breadcrumb{left:49px;top:92px;color:var(--white);font-family:"Raleway",sans-serif;font-weight:600;font-size:10px}
/* offices */
.office-map{width:258px;height:121px;border:2px solid #222;background:linear-gradient(135deg,#e6e3dc,#d6d3cc)}
.office-title{left:353px;font-family:"Raleway",sans-serif;font-weight:500;font-size:19.5px;color:var(--title-blue)}
.office-line{left:355px;display:flex;align-items:flex-start;gap:8px;font-size:12px;color:var(--ink);line-height:15.5px}
.office-line svg{fill:var(--blue);margin-top:2px;flex:none}
/* form */
.contact-section{left:0;top:619px;width:708px;height:274px;background:var(--form-bg)}
.section-title{left:0;top:47px;width:708px;text-align:center;font-family:"Raleway",sans-serif;font-weight:500;font-size:20px;letter-spacing:1.5px;color:var(--blue)}
.section-rule{left:297px;top:73px;width:105px;height:2px;background:var(--grey)}
.field{border:1.5px solid var(--field-border);background:var(--form-bg);font-size:9.5px;color:#444;padding:6px 18px}
.field.message{padding:6px 12px}
.send-btn{left:296px;top:201px;width:114px;height:25px;background:var(--blue);color:var(--white);font-size:10px;display:flex;align-items:center;justify-content:center;gap:5px}
/* footer */
.footer-band{left:0;top:893px;width:708px;height:27px;background:var(--band-grey)}
.footer-brand{left:0;top:920px;width:708px;height:75px;display:flex;align-items:center;justify-content:center;gap:8px;font-family:"Raleway",sans-serif;font-weight:500;font-size:44px;letter-spacing:2px;color:var(--sky)}
.footer-brand .brand-mark{width:14px;height:14px}
.site-footer{left:0;top:995px;width:708px;height:172px;background:var(--sky)}
.social-row{left:0;top:24px;width:708px;display:flex;justify-content:center;gap:8px}
.social-link{width:40px;height:40px;border:2px solid var(--white);border-radius:50%}
.firm-name{left:0;top:75px;width:708px;text-align:center;font-family:"Raleway",sans-serif;font-weight:500;font-size:19px;color:var(--ink)}
.footer-contact{left:0;width:708px;display:flex;justify-content:center;align-items:center;gap:7px;font-size:15px;font-weight:700;color:var(--white)}
.footer-contact svg{fill:var(--white)}
.copyright{left:0;top:1167px;width:708px;height:33px;background:var(--blue);color:var(--white);font-size:11.5px;display:flex;align-items:center;justify-content:center}
</style>
</head>
<body>

<div class="abs top-bar"></div>
<a class="abs consult-btn">REQUEST A FREE COSULTATION
  <svg width="11" height="8" viewBox="0 0 11 8"><path d="M0 3.3h8V1l3 3-3 3V4.7H0z" fill="#fff"/></svg></a>

<header class="abs site-header">
  <div class="abs brand"><span>MOLAW</span><span class="brand-mark"></span></div>
  <nav class="abs main-nav">
    <a class="nav-item"><svg width="10" height="9" viewBox="0 0 10 9"><path d="M5 0 10 4.5H8.5V9H6V6H4v3H1.5V4.5H0z"/></svg>Home</a>
    <a class="nav-item"><svg width="10" height="10" viewBox="0 0 10 10"><path d="M1 5 5 1l2 2-4 4zM5 5l1.3-1.3L10 7.5 8.7 8.8z"/></svg>About Us</a>
    <a class="nav-item"><svg width="11" height="9" viewBox="0 0 11 9"><path d="M4 0h3v1.5h4V9H0V1.5h4zM4.8.8v.7h1.4V.8z"/></svg>Practice Areas</a>
    <a class="nav-item active"><svg width="9" height="9" viewBox="0 0 9 9"><path d="M1.8 0 3.3 2.3 2.4 3.4Q3.5 5.6 5.6 6.6l1.1-.9L9 7.2 7.8 9Q2.5 8.2 0 1.2z"/></svg>Contact Us</a>
  </nav>
</header>

<section class="abs page-hero" role="img" aria-label="California vineyard hills at dusk">
  <h1 class="abs hero-title">Contact Us</h1>
  <div class="abs hero-rule"></div>
  <p class="abs breadcrumb">Home / Contact Us</p>
</section>

<section class="offices">
  <div class="abs office-map" style="left:70px;top:298px" role="img" aria-label="Street map of the Sacramento office location"></div>
  <h2 class="abs office-title" style="top:300px">Sacramento Area Office:</h2>
  <p class="abs office-line" style="top:333px"><svg width="7" height="10" viewBox="0 0 7 10"><path d="M3.5 0A3.5 3.5 0 0 0 0 3.5C0 6 3.5 10 3.5 10S7 6 7 3.5A3.5 3.5 0 0 0 3.5 0zm0 5a1.5 1.5 0 1 1 0-3 1.5 1.5 0 0 1 0 3z"/></svg><span>418 Capitol Row, Suite 210<br>Sacramento, CA 95811</span></p>
  <p class="abs office-line" style="top:369px"><svg width="10" height="10" viewBox="0 0 9 9"><path d="M1.8 0 3.3 2.3 2.4 3.4Q3.5 5.6 5.6 6.6l1.1-.9L9 7.2 7.8 9Q2.5 8.2 0 1.2z"/></svg>(916) 555-0142</p>
  <p class="abs office-line" style="top:397px"><svg width="12" height="9" viewBox="0 0 12 9"><path d="M0 0h12v1.2L6 5 0 1.2zm0 2.6 6 3.8 6-3.8V9H0z"/></svg>info@marwickostrand.com</p>

  <div class="abs office-map" style="left:70px;top:447px" role="img" aria-label="Street map of the Bay Area office location"></div>
  <h2 class="abs office-title" style="top:446px">Bay Area Office:</h2>
  <p class="abs office-line" style="top:479px"><svg width="7" height="10" viewBox="0 0 7 10"><path d="M3.5 0A3.5 3.5 0 0 0 0 3.5C0 6 3.5 10 3.5 10S7 6 7 3.5A3.5 3.5 0 0 0 3.5 0zm0 5a1.5 1.5 0 1 1 0-3 1.5 1.5 0 0 1 0 3z"/></svg><span>7400 Oakfield Center Drive<br>Pleasanton, CA 94588</span></p>
  <p class="abs office-line" style="top:517px"><svg width="10" height="10" viewBox="0 0 9 9"><path d="M1.8 0 3.3 2.3 2.4 3.4Q3.5 5.6 5.6 6.6l1.1-.9L9 7.2 7.8 9Q2.5 8.2 0 1.2z"/></svg>(925) 555-0187</p>
  <p class="abs office-line" style="top:541px"><svg width="12" height="9" viewBox="0 0 12 9"><path d="M0 0h12v1.2L6 5 0 1.2zm0 2.6 6 3.8 6-3.8V9H0z"/></svg>info@marwickostrand.com</p>
</section>

<section class="abs contact-section">
  <h2 class="abs section-title">Contact Us</h2>
  <div class="abs section-rule"></div>
  <div class="abs field" style="left:62px;top:98px;width:285px;height:25px">Name</div>
  <div class="abs field" style="left:62px;top:128px;width:285px;height:25px">Email</div>
  <div class="abs field" style="left:62px;top:157px;width:285px;height:25px">Phone</div>
  <div class="abs field message" style="left:355px;top:98px;width:286px;height:84px">Message</div>
  <a class="abs send-btn">Send Message
    <svg width="10" height="7" viewBox="0 0 11 8"><path d="M0 3.3h8V1l3 3-3 3V4.7H0z" fill="#fff"/></svg></a>
</section>

<div class="abs footer-band"></div>
<div class="abs footer-brand"><span>MOLAW</span><span class="brand-mark"></span></div>

<footer class="abs site-footer">
  <div class="abs social-row">
    <a class="social-link" aria-label="Social profile 1"></a>
    <a class="social-link" aria-label="Social profile 2"></a>
    <a class="social-link" aria-label="Social profile 3"></a>
    <a class="social-link" aria-label="Social profile 4"></a>
    <a class="social-link" aria-label="Social profile 5"></a>
  </div>
  <p class="abs firm-name">MARWICK &amp; OSTRAND LAW</p>
  <p class="abs footer-contact" style="top:112px"><svg width="14" height="14" viewBox="0 0 14 14"><path d="M0 2h3v12H0zM4 0h7v4h3v10H4zm2 1.5V4h3.5V1.5zM6 6v2h2V6zm3 0v2h2V6zM6 9v2h2V9zm3 0v2h2V9z"/></svg>(916) 555-0143</p>
  <p class="abs footer-contact" style="top:134px"><svg width="15" height="11" viewBox="0 0 12 9"><path d="M0 0h12v1.2L6 5 0 1.2zm0 2.6 6 3.8 6-3.8V9H0z"/></svg>info@marwickostrand.com</p>
</footer>

<div class="abs copyright">© 2017 copyright</div>

</body>
</html>
```